design cheese package for ORVEN

We want someone to give me some graphic designs for the cheese package. You shall not only design it on the basis of our product sizes, but also the design with my company Logo shall be novel and attactive. There are some pictures in the attachments: picture 1--3 for my product; picture 4 for my company Logo; picture 5--6 for your reference Thanks! please add the word ORVEN in the package design, thanks!

```html
<!DOCTYPE html>
<html lang="en">
<head>
<meta charset="utf-8">
<title>ORVEN Gouda Label</title>
<link href="https://fonts.googleapis.com/css2?family=Lilita+One&display=swap" rel="stylesheet">
<style>
  :root {
    --backdrop: #a89e8a;
    --label-cream: #fde6c6;
    --label-orange: #f7931e;
    --label-deep-orange: #f07a12;
    --rim-red: #e2450f;
    --rim-dark: #2a160c;
    --brand-green: #1d3323;
    --badge-fill: #dfe9d6;
    --text-white: #ffffff;
    --text-shadow: rgba(60, 25, 0, 0.55);
    --cheese-pale: #f6e58a;
    --cheese-yellow: #f1c84a;
    --wax-red: #d6141b;
  }
  html, body {
    margin: 0;
    padding: 0;
    width: 1200px;
    height: 1200px;
    overflow: hidden;
    background: var(--backdrop);
  }
  .canvas {
    position: relative;
    width: 1200px;
    height: 1200px;
    font-family: "Lilita One", "Arial Black", sans-serif;
  }
  .label-panel {
    position: absolute;
    left: 420px;
    top: 400px;
    width: 360px;
    height: 680px;
    box-sizing: border-box;
    background: linear-gradient(to bottom, var(--label-cream) 0%, #fbc98a 26%, var(--label-orange) 50%, var(--label-deep-orange) 100%);
    border: 5px solid var(--rim-red);
    border-radius: 0 0 30px 30px;
    box-shadow: 0 0 0 3px var(--rim-dark), 0 6px 14px rgba(0,0,0,0.25);
  }
  .brand-badge {
    position: absolute;
    left: 445px;
    top: 120px;
    width: 310px;
    height: 310px;
    border-radius: 50%;
    background: var(--badge-fill);
    border: 8px solid var(--brand-green);
    box-sizing: border-box;
  }
  .brand-name {
    position: absolute;
    left: 420px;
    top: 440px;
    width: 360px;
    text-align: center;
    font-size: 48px;
    letter-spacing: 2px;
    color: var(--brand-green);
    margin: 0;
  }
  .claim {
    position: absolute;
    left: 420px;
    top: 520px;
    width: 360px;
    text-align: center;
    margin: 0;
    font-size: 54px;
    line-height: 50px;
    color: var(--text-white);
    text-shadow: 2px 3px 3px var(--text-shadow);
  }
  .cheese-photo {
    position: absolute;
    left: 495px;
    top: 700px;
    width: 210px;
    height: 240px;
    border-radius: 14px 40px 10px 10px;
    background: linear-gradient(100deg, var(--cheese-pale) 0%, var(--cheese-yellow) 68%, var(--wax-red) 74%, #a50d12 100%);
    box-shadow: 0 10px 12px rgba(90, 40, 0, 0.35);
  }
  .variety {
    position: absolute;
    left: 420px;
    top: 955px;
    width: 360px;
    text-align: center;
    margin: 0;
    font-size: 88px;
    line-height: 96px;
    color: var(--text-white);
    text-shadow: 2px 4px 4px var(--text-shadow);
  }
</style>
</head>
<body>
  <main class="canvas">
    <div class="label-panel"></div>
    <div class="brand-badge" role="img" aria-label="Brand badge area: cow in a green field with a windmill"></div>
    <p class="brand-name">ORVEN</p>
    <h2 class="claim">ALL<br>NATURAL<br>CHEESE</h2>
    <div class="cheese-photo" role="img" aria-label="Photo of a gouda cheese wedge with red wax rind"></div>
    <h1 class="variety">GOUDA</h1>
  </main>
</body>
</html>
```